Real Estate Company Looking for Business Card Designs for 3 Executives

Hello!
Thanks so much for considering our project! We are a real estate investment company located in Edmonton, Alberta called Bellcrane Group of Companies. We invest/develop both commercial and residential real estate and are looking to create 3 DOUBLE-SIDED business cards for 3 top executives in the company! (for some reason it won't let us select the double-sided option, but yes, the cards are double sided and would be happy to tip extra)

We have certain guidelines that we want our business cards to for sure follow - the back of the Business card has to be the Black Background Version of the Logo which has already been designed and linked as a file (first file). We want the entire back of the card to simply just be the black background logo. In terms of the front of the card, would like to see a smaller version of the white background logo (linked as the second file) in the top left hand corner - of course, feel free to get creative and we can make revisions together along the way! and Then after that, just text. We want the card to be sharp, clean, easy on the eyes and highly professional looking. We would like the card to include the Full name of the Company (Bellcrane Group of Companies), Name of the Person, Title, Phone, Email. If possible please provide the front part of the card for 3 people:

1) Bellcrane Group of Companies, Nora Lindqvist, Chief Financial Officer, 780-555-0142, noralindqvist@bellcranegroup.example

2) Bellcrane Group of Companies, Julien Lindqvist, Chief Executive Officer, 780-555-0187, julienlindqvist@bellcranegroup.example

3) Bellcrane Group of Companies, Tom Okafor, Chief Operations Officer, 587-555-0163, tomokafor@bellcranegroup.example

Thank you so much for considering our project & we look forward to seeing your designs!

```html
<!DOCTYPE html>
<html lang="en">
<head>
<meta charset="utf-8">
<title>Bellcrane Group of Companies – Business Card</title>
<link rel="stylesheet" href="https://fonts.googleapis.com/css2?family=Arimo:wght@400&family=Tinos:wght@700&display=swap">
<style>
  :root {
    --backdrop: #161616;
    --card: #202020;
    --ink: #ffffff;
    --ink-soft: #f2f2f2;
    --emboss: #383838;
  }
  * { margin: 0; padding: 0; box-sizing: border-box; }
  html, body {
    width: 1200px; height: 1059px; overflow: hidden;
    background: var(--backdrop);
  }
  .canvas { position: relative; width: 1200px; height: 1059px; }
  .card {
    position: absolute;
    background: var(--card);
  }
  .card--front { left: 257px; top: 89px; width: 687px; height: 390px; }
  .card--back  { left: 254px; top: 546px; width: 693px; height: 394px; }

  .brand {
    position: absolute; left: 89px; top: 128px; width: 200px;
    display: flex; flex-direction: column; align-items: center;
    color: var(--ink);
    font-family: "Arimo", Arial, sans-serif; font-weight: 400;
  }
  .brand__mark {
    width: 14px; height: 14px; background: var(--ink); margin-bottom: 12px;
  }
  .brand__name { font-size: 27px; letter-spacing: 5px; line-height: 1; }
  .brand__sub { font-size: 9px; letter-spacing: 2.4px; margin-top: 8px; }

  .divider {
    position: absolute; left: 321px; top: 123px;
    width: 1.5px; height: 145px; background: var(--ink);
  }

  .person {
    position: absolute; left: 350px; top: 117px; color: var(--ink);
  }
  .person__name {
    font-family: "Tinos", "Times New Roman", serif; font-weight: 700;
    font-size: 26px; letter-spacing: 0.6px; line-height: 1.1;
  }
  .person__title {
    font-family: "Arimo", Arial, sans-serif; font-size: 16.5px;
    color: var(--ink-soft); margin-top: 2px;
  }
  .contacts {
    list-style: none; margin-top: 30px;
    font-family: "Arimo", Arial, sans-serif; font-size: 16.5px; color: var(--ink-soft);
  }
  .contacts li { display: flex; align-items: center; height: 26px; }
  .contacts svg { width: 13px; height: 13px; margin-right: 7px; fill: var(--ink); flex: none; }

  .back-brand {
    position: absolute; inset: 0;
    display: flex; flex-direction: column; align-items: center; justify-content: center;
    font-family: "Arimo", Arial, sans-serif; font-weight: 400; color: var(--emboss);
  }
  .back-brand__name { font-size: 62px; letter-spacing: 10px; line-height: 1; }
  .back-brand__sub { font-size: 16px; letter-spacing: 6px; margin-top: 14px; }
</style>
</head>
<body>
<main class="canvas">
  <section class="card card--front" aria-label="Card front">
    <div class="brand">
      <span class="brand__mark"></span>
      <span class="brand__name">BELLCRANE</span>
      <span class="brand__sub">GROUP OF COMPANIES</span>
    </div>
    <div class="divider"></div>
    <div class="person">
      <h1 class="person__name">NORA LINDQVIST</h1>
      <p class="person__title">Chief Financial Officer</p>
      <ul class="contacts">
        <li>
          <svg viewBox="0 0 24 24" aria-hidden="true"><path d="M6.6 10.8a15.1 15.1 0 0 0 6.6 6.6l2.2-2.2c.3-.3.7-.4 1-.2 1.1.4 2.3.6 3.6.6.6 0 1 .4 1 1V20c0 .6-.4 1-1 1A17 17 0 0 1 3 4c0-.6.4-1 1-1h3.5c.6 0 1 .4 1 1 0 1.3.2 2.5.6 3.6.1.3 0 .7-.2 1z"/></svg>
          780-555-0142
        </li>
        <li>
          <svg viewBox="0 0 24 24" aria-hidden="true"><path d="M2 5h20v14H2zm2 2v.3l8 5.2 8-5.2V7zm0 2.7V17h16V9.7l-8 5.2z"/></svg>
          noralindqvist@bellcranegroup.example
        </li>
        <li>
          <svg viewBox="0 0 24 24" aria-hidden="true"><path d="M12 2a10 10 0 1 0 0 20 10 10 0 0 0 0-20zm-1 17.9A8 8 0 0 1 4.2 10L9 14.8v1a2 2 0 0 0 2 2zm6.9-2.5A2 2 0 0 0 16 16h-1v-3a1 1 0 0 0-1-1H8v-2h2a1 1 0 0 0 1-1V7h2a2 2 0 0 0 2-2v-.4a8 8 0 0 1 2.9 12.8z"/></svg>
          www.bellcranegroup.example
        </li>
      </ul>
    </div>
  </section>

  <section class="card card--back" aria-label="Card back">
    <div class="back-brand">
      <span class="back-brand__name">BELLCRANE</span>
      <span class="back-brand__sub">GROUP OF COMPANIES</span>
    </div>
  </section>
</main>
</body>
</html>
```